Real Estate Managemene Company Needs Business Card Design

We have a logo design and just need business cards made now for our business. Please use PDF logo # 3.

Card with Information to be attached shortly.

The card is used for a real estate management company. We will need to add four other employees and their cards.

Industry/Entity Type

Real Estate

Contact Information for Business Card

Tariq Hamdan
President
3187 Thornwick Avenue
Suite C
Glendale Heights, IL 60152
Phone 630.417.2286
Fax 630.417.2287
Cell 630.473.8062
vantorp@mailbreeze.net

Once design is approved we will have four other employees
Omar Hamdan
Operations Manager

Nadia Hamdan
Administrative Manager

Faz Hamdan
Principal

We would need to take out the cell # 630.473.8062 out for the remaining three cards.

Requirements
Must have
• Please use logo attached

```html
<!DOCTYPE html>
<html lang="en">
<head>
<meta charset="utf-8">
<title>Business Card – Larkmoor Property Management Group</title>
<link href="https://fonts.googleapis.com/css2?family=Open+Sans:wght@300;400;600;700&display=swap" rel="stylesheet">
<style>
  :root {
    --page-bg: #e6e4e0;
    --card-white: #ffffff;
    --card-shade: #eeeeee;
    --ink-dark: #3a3a3a;
    --ink-mid: #5a5a5a;
    --ink-soft: #8a8a8a;
    --wave-black: #1c1c1c;
    --wave-grey: #6b6b6b;
    --accent-blue: #2c7fb8;
  }
  * { margin: 0; padding: 0; box-sizing: border-box; }
  html, body {
    width: 1200px; height: 909px; overflow: hidden;
    background: var(--page-bg);
    font-family: "Open Sans", Arial, sans-serif;
  }
  .card {
    position: absolute; left: 75px; top: 154px;
    width: 1050px; height: 600px;
    background: linear-gradient(160deg, var(--card-white) 0%, var(--card-shade) 100%);
    box-shadow: 0 10px 30px rgba(0,0,0,0.18);
    overflow: hidden;
  }
  .card-wave { position: absolute; inset: 0; width: 1050px; height: 600px; }
  .brand {
    position: absolute; left: 90px; top: 290px;
    display: flex; align-items: center; gap: 16px;
  }
  .brand-mark { width: 34px; height: 34px; background: var(--accent-blue); }
  .brand-name {
    font-weight: 600; font-size: 26px; line-height: 1.2;
    color: var(--ink-dark); letter-spacing: 0.5px;
  }
  .divider {
    position: absolute; left: 530px; top: 150px;
    width: 1px; height: 150px;
    background: linear-gradient(to bottom, transparent, var(--ink-soft), transparent);
  }
  .contact {
    position: absolute; left: 560px; top: 72px;
    color: var(--ink-mid);
  }
  .contact-name { font-weight: 700; font-size: 25px; color: var(--ink-dark); line-height: 1.2; }
  .contact-title { font-weight: 400; font-size: 21px; color: var(--ink-soft); margin-bottom: 24px; }
  .contact-address { font-weight: 300; font-size: 22px; line-height: 1.4; margin-bottom: 14px; }
  .contact-lines { list-style: none; font-weight: 400; font-size: 22px; line-height: 1.45; }
  .contact-lines li { display: flex; align-items: center; gap: 16px; }
  .contact-lines svg { width: 19px; height: 19px; fill: var(--ink-dark); flex: none; }
</style>
</head>
<body>
  <div class="card">
    <svg class="card-wave" viewBox="0 0 1050 600" aria-hidden="true">
      <defs>
        <linearGradient id="greyFade" x1="0" y1="0" x2="1" y2="0">
          <stop offset="0" stop-color="#8a8a8a"/>
          <stop offset="0.6" stop-color="#d8d8d8"/>
          <stop offset="1" stop-color="#ffffff" stop-opacity="0"/>
        </linearGradient>
      </defs>
      <path d="M0,600 L0,480 C200,560 380,575 560,570 L560,600 Z" fill="url(#greyFade)"/>
      <path d="M0,600 L0,565 C320,595 640,575 800,505 C900,455 990,320 1050,185 L1050,600 Z" fill="var(--wave-grey)"/>
      <path d="M360,600 C600,592 840,530 925,435 C975,365 1015,260 1050,160 L1050,182 C1018,275 985,375 940,448 C860,548 640,594 430,600 Z" fill="var(--accent-blue)"/>
      <path d="M460,600 C660,592 865,540 955,452 C1003,385 1032,290 1050,210 L1050,600 Z" fill="var(--wave-black)"/>
    </svg>

    <div class="brand">
      <span class="brand-mark"></span>
      <span class="brand-name">Larkmoor Property<br>Management Group</span>
    </div>

    <div class="divider"></div>

    <div class="contact">
      <p class="contact-name">Tariq Hamdan</p>
      <p class="contact-title">President</p>
      <p class="contact-address">3187 Thornwick Avenue<br>Suite C<br>Glendale Heights, IL 60152</p>
      <ul class="contact-lines">
        <li><svg viewBox="0 0 24 24"><path d="M6.6 10.8c1.4 2.8 3.8 5.1 6.6 6.6l2.2-2.2c.3-.3.7-.4 1-.2 1.1.4 2.3.6 3.6.6.6 0 1 .4 1 1V20c0 .6-.4 1-1 1C10.6 21 3 13.4 3 4c0-.6.4-1 1-1h3.5c.6 0 1 .4 1 1 0 1.3.2 2.5.6 3.6.1.3 0 .7-.2 1L6.6 10.8z"/></svg>630.417.2286</li>
        <li><svg viewBox="0 0 24 24"><path d="M7 2h10c1.1 0 2 .9 2 2v16c0 1.1-.9 2-2 2H7c-1.1 0-2-.9-2-2V4c0-1.1.9-2 2-2zm0 3v13h10V5H7zm5 14.2a1 1 0 100 2 1 1 0 000-2z"/></svg>630.473.8062</li>
        <li><svg viewBox="0 0 24 24"><path d="M6 3h9v5H6zM4 9h16c1.1 0 2 .9 2 2v8c0 1.1-.9 2-2 2H4c-1.1 0-2-.9-2-2v-8c0-1.1.9-2 2-2zm2 3v2h3v-2H6zm0 4v2h3v-2H6zm5-4v2h3v-2h-3zm0 4v2h3v-2h-3z"/></svg>630.417.2287</li>
        <li><svg viewBox="0 0 24 24"><path d="M12 2a10 10 0 100 20h5v-2h-5a8 8 0 118-8v1.4c0 .8-.7 1.6-1.5 1.6S17 14.2 17 13.4V12a5 5 0 10-1.5 3.5 3.5 3.5 0 003 1.5c1.9 0 3.5-1.6 3.5-3.6V12A10 10 0 0012 2zm0 13a3 3 0 110-6 3 3 0 010 6z"/></svg>vantorp@mailbreeze.net</li>
      </ul>
    </div>
  </div>
</body>
</html>
```